KT Automation - Stationery and Identity.

Corporate Identity Design for the company, which includes Power Point presentations, Letterheads, business cards and mail signatures. We look for a simple design, but modern and elegant, that goes hand in hand with the technology that is the engine of the company.

Target Market(s)

Industrial Sector of Automation, Robotics and Process Control.

Industry/Entity Type

Automation

Colors

Designer to choose colors to be used in the design.

Requirements
Must have
• It must have an elegant, simple and clean design.

```html
<!DOCTYPE html>
<html lang="en">
<head>
<meta charset="utf-8">
<title>KT Automation – Stationery and Identity</title>
<link href="https://fonts.googleapis.com/css2?family=Roboto:wght@300;400;500;700&family=Roboto+Condensed:wght@400;700&display=swap" rel="stylesheet">
<style>
:root{
  --bg:#e3e3e3;
  --paper:#fafafa;
  --slide:#e9e9e9;
  --blue:#1a73c0;
  --blue-dark:#0c56a0;
  --blue-light:#3b9be0;
  --navy:#1c2e47;
  --gray:#9b9b9b;
  --gray-light:#c9c9c9;
  --ink:#4a4a4a;
  --muted:#8a8a8a;
  --white:#ffffff;
}
*{margin:0;padding:0;box-sizing:border-box}
html,body{width:988px;height:1200px;overflow:hidden}
body{background:var(--bg);position:relative;font-family:"Roboto",sans-serif;color:var(--ink)}
.piece{position:absolute;overflow:hidden}
.label{position:absolute;font-size:12px;color:#333;text-align:center}

/* brand mark */
.brand{display:flex;align-items:center;gap:5px;font-family:"Roboto",sans-serif;font-weight:300;letter-spacing:1.5px;text-transform:uppercase;white-space:nowrap}
.brand .dot{display:inline-block;background:var(--blue)}
.brand.stack{flex-direction:column;gap:6px}

/* letterhead */
.letterhead{left:60px;top:42px;width:470px;height:660px;background:var(--paper);box-shadow:0 1px 3px rgba(0,0,0,.15)}
.letterhead .brand{position:absolute;left:42px;top:52px;color:var(--gray);font-size:10px}
.letterhead .brand .dot{width:30px;height:30px}
.letterhead .contact{position:absolute;left:305px;top:42px;font-size:6.5px;line-height:9.2px;color:#555;padding-left:8px;border-left:1px solid var(--gray-light);height:76px}
.letterhead .contact .ic{color:var(--blue);display:inline-block;width:10px}
.letterhead .greeting{position:absolute;left:42px;top:186px;font-size:12px;font-weight:300;color:#333}
.letterhead .body{position:absolute;left:42px;top:218px;width:430px;font-size:6.3px;line-height:10px;font-weight:300;color:#555}
.letterhead .body p{margin-bottom:9px}
.letterhead .closing{position:absolute;left:42px;top:432px;font-size:6.5px;color:#555}
.letterhead .signature{position:absolute;left:38px;top:452px;width:90px;height:42px;background:linear-gradient(90deg,#e4ebf5,#eef2f8);border-radius:4px}
.letterhead .footer{position:absolute;left:0;bottom:0;width:100%;height:16px;background:linear-gradient(90deg,var(--blue-dark),var(--blue-light) 60%,var(--blue-dark));color:var(--white);font-size:7px;line-height:16px;padding-left:138px}
.letterhead .footer .sq{position:absolute;right:72px;top:3px;width:10px;height:10px;background:var(--white)}

/* front card */
.card-front{left:472px;top:146px;width:276px;height:157px;background:linear-gradient(110deg,#15263d 0%,#1f4670 45%,#3c79b6 100%);color:var(--white)}
.card-front .panel{position:absolute;right:0;top:0;width:170px;height:100%;background:linear-gradient(160deg,rgba(255,255,255,.05),rgba(220,230,240,.55));clip-path:polygon(30% 0,100% 0,100% 100%,30% 100%,0 50%)}
.person-name{font-weight:500;letter-spacing:.3px}
.person-role{font-weight:300;opacity:.85}
.card-front .person-name{position:absolute;left:14px;top:16px;font-size:11px}
.card-front .person-role{position:absolute;left:14px;top:28px;font-size:6.5px}
.card-front .addr{position:absolute;left:14px;top:66px;font-size:6.3px;line-height:8.4px;opacity:.8}
.card-front .lines{position:absolute;left:14px;top:108px;font-size:6.3px;line-height:8.8px;opacity:.85}
.card-front .brand{position:absolute;left:135px;top:70px;color:#333;font-size:8.5px}
.card-front .brand .dot{width:12px;height:12px;background:var(--navy)}

/* back card */
.card-back{left:472px;top:332px;width:274px;height:157px;background:radial-gradient(circle at 50% 45%,#3a97dc,var(--blue) 55%,var(--blue-dark));color:var(--white)}
.card-back .brand{position:absolute;left:0;right:0;top:40px;color:var(--white);font-size:10px;font-weight:400}
.card-back .brand .dot{width:40px;height:40px;background:var(--white)}
.card-back .web{position:absolute;left:0;right:0;bottom:19px;text-align:center;font-size:6.5px}

/* email signature option 2 */
.sig-vertical{left:771px;top:146px;width:166px;height:341px;background:var(--white);text-align:center;box-shadow:0 1px 3px rgba(0,0,0,.12)}
.sig-vertical .person-name{margin-top:46px;font-size:13px;color:var(--blue);font-weight:700}
.sig-vertical .person-role{font-size:7.5px;color:var(--muted)}
.sig-vertical .addr{margin-top:19px;font-size:7px;line-height:9.4px;color:#555}
.sig-vertical .lines{margin-top:15px;font-size:7px;line-height:10px;color:#555}
.sig-vertical .lines b{color:var(--blue);font-weight:500}
.sig-vertical .brand{position:absolute;left:0;right:0;top:208px;color:var(--gray);font-size:9.5px}
.sig-vertical .brand .dot{width:40px;height:40px}
.sig-vertical .foot{position:absolute;left:0;bottom:0;width:100%;height:12px;background:linear-gradient(90deg,var(--blue) 65%,var(--gray) 65%)}

/* email signature option 1 */
.sig-wide{left:561px;top:521px;width:376px;height:182px;background:linear-gradient(100deg,var(--blue-dark),var(--blue) 40%,var(--blue-light) 62%,var(--gray) 62%);color:var(--white)}
.sig-wide .panel{position:absolute;left:175px;top:10px;width:180px;height:172px;background:linear-gradient(135deg,rgba(255,255,255,.92),rgba(225,236,246,.92));clip-path:polygon(20% 0,85% 0,100% 50%,85% 100%,20% 100%,0 50%)}
.sig-wide .person-name{position:absolute;left:24px;top:14px;font-size:13px}
.sig-wide .person-role{position:absolute;left:24px;top:29px;font-size:8px}
.sig-wide .addr{position:absolute;left:24px;top:74px;font-size:7.8px;line-height:10.4px}
.sig-wide .lines{position:absolute;left:24px;top:125px;font-size:7.8px;line-height:10.6px}
.sig-wide .brand{position:absolute;left:210px;top:80px;color:var(--gray);font-size:10px}
.sig-wide .brand .dot{width:14px;height:14px}

/* slides */
.slide{width:270px;height:203px;background:var(--slide);box-shadow:0 1px 3px rgba(0,0,0,.12)}
.slide .band{position:absolute;left:0;bottom:0;width:100%;height:4px;background:linear-gradient(90deg,var(--blue-dark),var(--blue-light) 70%,var(--gray) 70%)}
.slide .title{position:absolute;left:15px;top:12px;font-size:11.5px;font-weight:500;color:var(--blue)}
.slide .sub{position:absolute;left:15px;top:27px;font-size:5.5px;color:var(--muted)}
.slide .rule{position:absolute;left:15px;right:18px;top:36px;height:1px;background:var(--gray-light)}
.slide .mini{position:absolute;right:20px;top:16px;width:14px;height:14px;background:var(--blue)}
.tiny{font-size:3.8px;line-height:5.4px;color:#555}
.s1{left:62px;top:740px}.s2{left:362px;top:740px}.s3{left:663px;top:740px}
.s4{left:62px;top:958px}.s5{left:362px;top:958px}.s6{left:663px;top:958px}

.s1 .brand{position:absolute;left:0;right:0;top:30px;color:var(--gray);font-size:10px}
.s1 .brand .dot{width:46px;height:46px}
.s1 .hero{position:absolute;left:0;top:133px;width:100%;height:70px;background:linear-gradient(90deg,var(--blue-dark),var(--blue) 60%,var(--gray) 80%)}
.s1 .hero-text{position:absolute;left:21px;top:8px;font-family:"Roboto Condensed",sans-serif;color:var(--white);line-height:19px}
.s1 .hero-text .l1,.s1 .hero-text .l3{font-size:13px}
.s1 .hero-text .l2{font-size:15.5px;font-weight:700}

.s2 .intro{position:absolute;left:17px;top:52px;width:236px}
.s2 .team{position:absolute;left:13px;top:82px;display:flex;gap:3px}
.member{width:59px}
.member .photo{width:57px;height:50px;background:linear-gradient(160deg,#b9c3cc,#6d7680);clip-path:polygon(25% 0,75% 0,100% 50%,75% 100%,25% 100%,0 50%)}
.member .name{margin-top:12px;font-size:5.2px;color:var(--blue);font-weight:500}
.member .role{font-size:4.2px;color:var(--muted);margin-bottom:2px}

.s3 .cols{position:absolute;left:16px;top:51px;display:grid;grid-template-columns:120px 120px;column-gap:14px;row-gap:8px}
.s3 .g h4{font-size:5.6px;color:var(--blue);font-weight:500;margin-bottom:2px}

.s4 .top{position:absolute;left:17px;top:44px;width:236px}
.s4 .chart{position:absolute;left:14px;top:70px}
.s4 .bottom{position:absolute;left:17px;top:155px;width:236px}

.s5 .text{position:absolute;left:17px;top:50px;width:116px}
.s5 .text p{margin-bottom:6px}
.s5 .donut{position:absolute;left:152px;top:50px}
.s5 .legend{position:absolute;left:157px;top:131px;font-size:3.8px;line-height:6px;color:#555}
.s5 .legend i{display:inline-block;width:4px;height:4px;margin-right:3px;vertical-align:middle}

.s6{background:radial-gradient(circle at 50% 40%,#3a97dc,var(--blue) 55%,var(--blue-dark));text-align:center;color:var(--white)}
.s6 .thanks{position:absolute;left:0;right:0;top:66px;font-size:41px;font-weight:300;line-height:44px;padding-left:60px}
.s6 .coming{position:absolute;left:0;right:0;top:108px;font-size:22px;font-weight:300;padding-left:60px}
.s6 .foot{position:absolute;left:0;right:0;bottom:14px;font-size:3.8px;line-height:6px;opacity:.9}
</style>
</head>
<body>

<!-- Letterhead -->
<section class="piece letterhead">
  <div class="brand stack"><span class="dot"></span>KT Automation</div>
  <div class="contact">
    Calle Robles No. 410<br>
    Col. Vista Norte C.P. 45210<br>
    Zapopan, Jalisco, Mexico<br>
    <span class="ic">&#9742;</span>(+52) 33-5550-0142<br>
    <span class="ic">&#9647;</span>33-5550-0199<br>
    <span class="ic">&#9993;</span>dreyes@ktautomation.com
  </div>
  <div class="greeting">Dear Mr. Reyes,</div>
  <div class="body">
    <p>Thank you for your recent visit to our plant in Zapopan. We were glad to show your team our new robotic cell and the control systems we build for packaging lines. As discussed, we are preparing a proposal for the upgrade of your filling stations.</p>
    <p>Our engineers will review the current layout, the sensors in use and the network that links each station to your control room. We expect to share a first draft within two weeks, with a clear schedule and cost for every stage.</p>
    <p>During the project we will keep your production running. Each change is tested in our lab before it reaches your floor, and your staff will receive hands-on training on the new panels, alarms and reports.</p>
    <p>If you have any questions, please contact me directly at the number above. We look forward to working with you and your team on this project.</p>
  </div>
  <div class="closing">Sincerely,</div>
  <div class="signature" role="img" aria-label="Handwritten signature of Daniel Reyes"></div>
  <div class="footer">www.ktautomation.com<span class="sq"></span></div>
</section>
<div class="label" style="left:60px;top:710px;width:470px">Letterhead</div>

<!-- Business card front -->
<section class="piece card-front">
  <div class="panel"></div>
  <div class="person-name">DANIEL REYES</div>
  <div class="person-role">CEO / FOUNDER</div>
  <div class="addr">Calle Robles No. 410<br>Col. Vista Norte<br>C.P. 45210<br>Zapopan, Jalisco, Mexico</div>
  <div class="lines">&#9742; (+52) 33-5550-0142<br>&#9647; 33-5550-0199<br>&#9993; dreyes@ktautomation.com<br>&#9675; www.ktautomation.com</div>
  <div class="brand"><span class="dot"></span>KT Automation</div>
</section>
<div class="label" style="left:472px;top:312px;width:276px">Card</div>

<!-- Business card back -->
<section class="piece card-back">
  <div class="brand stack"><span class="dot"></span>KT Automation</div>
  <div class="web">www.ktautomation.com</div>
</section>
<div class="label" style="left:472px;top:496px;width:274px">BackCard</div>

<!-- Email signature option 2 -->
<section class="piece sig-vertical">
  <div class="person-name">DANIEL REYES</div>
  <div class="person-role">CEO / FOUNDER</div>
  <div class="addr">Calle Robles No. 410<br>Col. Vista Norte C.P. 45210<br>Zapopan, Jalisco, Mexico</div>
  <div class="lines"><b>P:</b> (+52) 33-5550-0142<br><b>C:</b> 33-5550-0199<br>dreyes@ktautomation.com<br>www.ktautomation.com</div>
  <div class="brand stack"><span class="dot"></span>KT Automation</div>
  <div class="foot"></div>
</section>
<div class="label" style="left:771px;top:497px;width:166px">Emailsignature Option-02</div>

<!-- Email signature option 1 -->
<section class="piece sig-wide">
  <div class="panel"></div>
  <div class="person-name">DANIEL REYES</div>
  <div class="person-role">CEO / FOUNDER</div>
  <div class="addr">Calle Robles No. 410<br>Col. Vista Norte<br>C.P. 45210<br>Zapopan, Jalisco, Mexico</div>
  <div class="lines">&#9742; (+52) 33-5550-0142<br>&#9647; 33-5550-0199<br>&#9993; dreyes@ktautomation.com<br>&#9675; www.ktautomation.com</div>
  <div class="brand"><span class="dot"></span>KT Automation</div>
</section>
<div class="label" style="left:561px;top:710px;width:376px;font-size:13px">Emailsignature Option-01</div>

<!-- Slide: title -->
<section class="piece slide s1">
  <div class="brand stack"><span class="dot"></span>KT Automation</div>
  <div class="hero">
    <div class="hero-text"><div class="l1">Welcome to Our</div><div class="l2">Presentation Name</div><div class="l3">Description</div></div>
  </div>
</section>

<!-- Slide: team -->
<section class="piece slide s2">
  <div class="title">Heading Here</div><div class="sub">Sub Heading</div><div class="rule"></div><div class="mini"></div>
  <p class="intro tiny">Our team brings years of field work in automation, robotics and process control for plants across the region. Every project is led by a senior engineer.</p>
  <div class="team">
    <div class="member"><div class="photo" role="img" aria-label="Portrait photo of team member 1"></div><div class="name">Team member1</div><div class="role">Title</div><p class="tiny">Leads design of control panels and plant networks.</p></div>
    <div class="member"><div class="photo" role="img" aria-label="Portrait photo of team member 2"></div><div class="name">Team member2</div><div class="role">Title</div><p class="tiny">Manages client projects from first visit to start-up.</p></div>
    <div class="member"><div class="photo" role="img" aria-label="Portrait photo of team member 3"></div><div class="name">Team member3</div><div class="role">Title</div><p class="tiny">Programs robots and tests each cell in our lab.</p></div>
    <div class="member"><div class="photo" role="img" aria-label="Portrait photo of team member 4"></div><div class="name">Team member4</div><div class="role">Title</div><p class="tiny">Handles training, support and service after delivery.</p></div>
  </div>
  <div class="band"></div>
</section>

<!-- Slide: groups -->
<section class="piece slide s3">
  <div class="title">Heading Here</div><div class="sub">Sub Heading</div><div class="rule"></div><div class="mini"></div>
  <div class="cols">
    <div class="g"><h4>Group1</h4><p class="tiny">Short note on this service area, its main benefits and the type of plant it fits best.</p></div>
    <div class="g"><h4>Group4</h4><p class="tiny">Short note on this service area, its main benefits and the type of plant it fits best.</p></div>
    <div class="g"><h4>Group2</h4><p class="tiny">Short note on this service area, its main benefits and the type of plant it fits best.</p></div>
    <div class="g"><h4>Group5</h4><p class="tiny">Short note on this service area, its main benefits and the type of plant it fits best.</p></div>
    <div class="g"><h4>Group3</h4><p class="tiny">Short note on this service area, its main benefits and the type of plant it fits best.</p></div>
    <div class="g"><h4>Group6</h4><p class="tiny">Short note on this service area, its main benefits and the type of plant it fits best.</p></div>
  </div>
  <div class="band"></div>
</section>

<!-- Slide: bar chart -->
<section class="piece slide s4">
  <div class="title">Heading Here</div><div class="sub">Sub Heading</div><div class="rule"></div><div class="mini"></div>
  <p class="top tiny">Monthly output of three test lines compared across four periods, measured in thousands of units.</p>
  <svg class="chart" width="240" height="82" viewBox="0 0 240 82">
    <defs><linearGradient id="barBlue" x1="0" y1="0" x2="0" y2="1"><stop offset="0" stop-color="#1a73c0"/><stop offset="1" stop-color="#4fb0ee"/></linearGradient></defs>
    <g stroke="#cfcfcf" stroke-width=".5">
      <line x1="12" y1="8" x2="236" y2="8"/><line x1="12" y1="17" x2="236" y2="17"/><line x1="12" y1="26" x2="236" y2="26"/><line x1="12" y1="35" x2="236" y2="35"/><line x1="12" y1="44" x2="236" y2="44"/><line x1="12" y1="53" x2="236" y2="53"/><line x1="12" y1="62" x2="236" y2="62"/><line x1="12" y1="71" x2="236" y2="71"/>
    </g>
    <g font-size="3" fill="#777" font-family="Roboto, sans-serif"><text x="4" y="9">5</text><text x="4" y="27">4</text><text x="4" y="45">3</text><text x="4" y="63">2</text><text x="4" y="72">0</text></g>
    <g>
      <rect x="22" y="24" width="7" height="47" fill="url(#barBlue)"/><rect x="33" y="31" width="7" height="40" fill="#a2a2a2"/><rect x="44" y="48" width="7" height="23" fill="url(#barBlue)"/>
      <rect x="83" y="40" width="7" height="31" fill="url(#barBlue)"/><rect x="94" y="18" width="7" height="53" fill="#a2a2a2"/><rect x="105" y="48" width="7" height="23" fill="url(#barBlue)"/>
      <rect x="144" y="25" width="7" height="46" fill="url(#barBlue)"/><rect x="155" y="31" width="7" height="40" fill="#a2a2a2"/><rect x="166" y="19" width="7" height="52" fill="url(#barBlue)"/>
      <rect x="205" y="9" width="7" height="62" fill="url(#barBlue)"/><rect x="216" y="31" width="7" height="40" fill="#a2a2a2"/><rect x="227" y="48" width="7" height="23" fill="url(#barBlue)"/>
    </g>
    <g font-size="3" fill="#777" font-family="Roboto, sans-serif"><text x="30" y="78">Category 1</text><text x="91" y="78">Category 2</text><text x="152" y="78">Category 3</text><text x="213" y="78">Category 4</text></g>
  </svg>
  <p class="bottom tiny">Line A kept steady growth while line B improved after the new sensor layout was installed in period two.</p>
  <div class="band"></div>
</section>

<!-- Slide: donut chart -->
<section class="piece slide s5">
  <div class="title">Heading Here</div><div class="sub">Sub Heading</div><div class="rule"></div><div class="mini"></div>
  <div class="text tiny">
    <p>This chart shows how our work is divided between service areas. Most projects combine robotics with process control, while a smaller share covers training and support.</p>
    <p>We plan to grow the support area next year with a new team based in our Zapopan office.</p>
  </div>
  <svg class="donut" width="70" height="70" viewBox="0 0 70 70">
    <g fill="none" stroke-width="11">
      <circle cx="35" cy="35" r="26" stroke="#1a73c0" stroke-dasharray="81.7 81.7" transform="rotate(-90 35 35)"/>
      <circle cx="35" cy="35" r="26" stroke="#9c9c9c" stroke-dasharray="81.7 81.7" stroke-dashoffset="81.7" transform="rotate(-90 35 35)"/>
    </g>
    <g stroke="#e9e9e9" stroke-width="1.6">
      <line x1="35" y1="3" x2="35" y2="20"/><line x1="35" y1="50" x2="35" y2="67"/><line x1="3" y1="35" x2="20" y2="35"/><line x1="50" y1="35" x2="67" y2="35"/>
      <line x1="12" y1="12" x2="24" y2="24"/><line x1="46" y1="46" x2="58" y2="58"/><line x1="58" y1="12" x2="46" y2="24"/><line x1="12" y1="58" x2="24" y2="46"/>
    </g>
    <circle cx="35" cy="35" r="10" fill="#3b9be0" stroke="#1a73c0" stroke-width="1.5"/>
  </svg>
  <div class="legend">
    <div><i style="background:var(--blue)"></i>Robotics cells 50%</div>
    <div><i style="background:var(--gray)"></i>Process control 50%</div>
    <div style="margin-top:3px">Figures based on last year of projects.</div>
  </div>
  <div class="band"></div>
</section>

<!-- Slide: closing -->
<section class="piece slide s6">
  <div class="thanks">Thanks</div>
  <div class="coming">For Coming</div>
  <div class="foot">Calle Robles No. 410, Col. Vista Norte C.P. 45210 Zapopan, Jalisco, Mexico<br>P: (+52) 33-5550-0142 M: 33-5550-0199 E: dreyes@ktautomation.com W: www.ktautomation.com</div>
</section>

</body>
</html>
```